Harbor Sushi & Steak Dinner Menu

I'm looking for a MENU design with a particular feel. I want to have a base template made that I can then use for future alterations to the menu; ie I can go in and change out different entrees as the menu changes but the template will remain the same. (Ideally it would be in an Apple Pages format.). Also ideally - dinner menu will occupy 2 pages 8.5 x 11. The restaurant's name is Harbor. It is a MODERN steak house that will also feature Sushi, a Raw Bar, Exquisite Cocktails and a sophisticated nightlife crowd. I have attached our LOGO, a secondary logo that we will be featuring throughout the project including on the menu cover (the gold U). Finally - I have attached the content that we would like to see. AGAIN - I REITERATE: High end dining and lounge atmosphere. A couple of restaurants / menus that I love are Morvendel in NYC and Pellucid Steakhouse in Long Island NY. Please do not duplicate - just trying to offer some suggestions.

Requirements
Must have
• A sophisticated and elegant feel without being stuffy or old.

```html
<!DOCTYPE html>
<html lang="en">
<head>
<meta charset="utf-8">
<title>Harbor Sushi &amp; Steak — Dinner Menu</title>
<link href="https://fonts.googleapis.com/css2?family=Federo&family=PT+Sans:wght@400;700&display=swap" rel="stylesheet">
<style>
  :root {
    --backdrop: #e9e4dc;
    --page: #0b0b0b;
    --page-sheen: #1c1c1c;
    --gold: #d8c06a;
    --gold-soft: #bfa653;
    --red: #d2213d;
    --ink: #f2f2f2;
    --ink-dim: #cfcfcf;
  }
  * { box-sizing: border-box; margin: 0; padding: 0; }
  html, body { width: 1200px; height: 840px; overflow: hidden; }
  body {
    background: var(--backdrop);
    font-family: "PT Sans", sans-serif;
    color: var(--ink);
    position: relative;
  }
  .menu-page {
    position: absolute;
    top: 72px;
    width: 570px;
    height: 740px;
    background: linear-gradient(135deg, var(--page) 0%, var(--page-sheen) 45%, var(--page) 100%);
  }
  .menu-page--food { left: 20px; }
  .menu-page--grill { left: 610px; }
  .page-tab {
    position: absolute;
    top: -38px;
    left: 50%;
    width: 200px;
    height: 80px;
    margin-left: -100px;
    border-radius: 100px 100px 0 0;
    background: var(--page);
  }
  .menu-page--grill .page-tab { left: 62%; }
  .dotted-rule {
    position: absolute;
    top: 22px; bottom: 22px;
    left: 14px; right: 14px;
    border-left: 3px dotted var(--gold);
    border-right: 3px dotted var(--gold);
  }
  .corner-mark {
    position: absolute;
    width: 7px; height: 7px;
    background: var(--gold);
    transform: rotate(45deg);
  }
  .corner-mark--tl { top: 12px; left: 12px; }
  .corner-mark--tr { top: 12px; right: 12px; }
  .corner-mark--bl { bottom: 12px; left: 12px; }
  .corner-mark--br { bottom: 12px; right: 12px; }

  .brand-name {
    font-family: "Federo", sans-serif;
    color: var(--gold);
    text-align: center;
    letter-spacing: 3px;
    white-space: nowrap;
  }
  .brand-name--head {
    position: absolute;
    top: -18px; left: 0; right: 0;
    font-size: 22px;
    line-height: 1.15;
  }
  .brand-name--foot {
    position: absolute;
    bottom: 58px; left: 0; right: 0;
    font-size: 26px;
  }

  .photo {
    position: absolute;
    border-radius: 4px;
  }
  .photo--sushi {
    top: 40px; right: 34px; width: 230px; height: 140px;
    background: radial-gradient(ellipse at 50% 50%, #5a5a5a 0%, #2a2a2a 55%, transparent 85%);
  }
  .photo--platter {
    bottom: 30px; right: 34px; width: 200px; height: 150px;
    background: radial-gradient(ellipse at 50% 50%, #4c4c4c 0%, #222 55%, transparent 85%);
  }
  .photo--steak {
    top: 150px; right: 30px; width: 300px; height: 230px;
    background: radial-gradient(ellipse at 55% 50%, #5e5e5e 0%, #2b2b2b 50%, transparent 82%);
  }

  .section { position: absolute; }
  .section-title {
    font-family: "Federo", sans-serif;
    color: var(--gold);
    font-size: 15px;
    letter-spacing: 1px;
    margin-bottom: 5px;
  }
  .item {
    font-size: 9.5px;
    line-height: 1.38;
    color: var(--ink-dim);
  }
  .item-name { color: var(--red); font-weight: 700; }
  .plain-list .item { color: var(--ink); font-weight: 700; font-size: 10.5px; }

  .raw-bar-box {
    position: absolute;
    top: 292px; right: 36px;
    width: 222px; height: 300px;
    border: 2px solid var(--gold);
    padding: 14px 16px;
    background: rgba(0,0,0,0.55);
  }
  .raw-bar-box .section-title { font-size: 13.5px; margin-top: 14px; }
  .raw-bar-box .section-title:first-child { margin-top: 0; }
  .raw-bar-box .item { color: var(--ink); }
</style>
</head>
<body>

<section class="menu-page menu-page--food" aria-label="Sushi and raw bar page">
  <div class="page-tab"></div>
  <div class="dotted-rule"></div>
  <span class="corner-mark corner-mark--tl"></span><span class="corner-mark corner-mark--tr"></span>
  <span class="corner-mark corner-mark--bl"></span><span class="corner-mark corner-mark--br"></span>
  <div class="brand-name brand-name--head">HARBOR<br><span style="font-size:11px;letter-spacing:4px">SUSHI &amp; STEAK</span></div>

  <div class="photo photo--sushi" role="img" aria-label="Black and white photo of assorted sushi on a board"></div>

  <div class="section" style="top:130px;left:40px;width:170px">
    <h2 class="section-title">Sushi / Sashimi</h2>
    <p class="item"><span class="item-name">Toro</span> ; blue fin tuna belly (gf)</p>
    <p class="item"><span class="item-name">Ebi</span> ; cooked shrimp (gf)</p>
    <p class="item"><span class="item-name">Hamachi</span> ; yellowtail (gf)</p>
    <p class="item"><span class="item-name">Uni</span> ; sea urchin (gf)</p>
    <p class="item"><span class="item-name">Hirame</span> ; fluke (gf)</p>
  </div>
  <div class="section" style="top:152px;left:210px;width:150px">
    <p class="item"><span class="item-name">Unigi</span> ; fresh water eel (gf)</p>
    <p class="item"><span class="item-name">Sake</span> ; salmon (gf)</p>
    <p class="item"><span class="item-name">Madai</span> ; red snapper (gf)</p>
    <p class="item"><span class="item-name">Maguro</span> ; tuna (gf)</p>
  </div>

  <div class="section" style="top:232px;left:40px;width:490px">
    <h2 class="section-title">Sushi Platters</h2>
    <p class="item"><span class="item-name">Small</span> : Five pieces assorted sushi, nine pieces sashimi, spicy tuna roll (gf)</p>
    <p class="item"><span class="item-name">Large</span> : Eight pieces assorted sushi, eighteen pieces of sashimi, alaskan roll, rainbow roll (gf)</p>
  </div>

  <div class="section" style="top:300px;left:40px;width:250px">
    <h2 class="section-title">Classic Rolls</h2>
    <p class="item"><span class="item-name">Yellowtail</span> ; inside out roll with scallions (gf)</p>
    <p class="item"><span class="item-name">Spicy Tuna or Salmon or Yellowtail</span> ; spicy mayo</p>
    <p class="item"><span class="item-name">California</span> : crab meat, cucumber and avocado (gf)</p>
    <p class="item"><span class="item-name">Vegetable</span> : avocado, cucumber, asparagus, pickled radish (gf)</p>
    <p class="item"><span class="item-name">Spider</span> : soft shell crab and avocado with eel sauce</p>
    <p class="item"><span class="item-name">Shrimp Tempura</span> : deep fried tempura shrimp, eel sauce</p>
    <p class="item"><span class="item-name">Alaskan</span> : salmon and avocado (gf)</p>
  </div>

  <div class="raw-bar-box">
    <div class="plain-list">
      <h2 class="section-title">Seafood Raw Bar</h2>
      <p class="item">Lobster Cocktail</p>
      <p class="item">Shrimp Cocktail</p>
      <p class="item">Clams on the Half Shell</p>
      <p class="item">Oysters on the Half Shell</p>
      <p class="item">Colossal Crab Cocktail</p>
    </div>
    <h2 class="section-title">Raw Bar Plate for One :</h2>
    <p class="item">Two shrimp, half of a one pound lobster, two clams, one east coast oyster, one west coast oyster</p>
    <h2 class="section-title">Seafood Platters</h2>
    <p class="item">Shrimp, oyster, clams, lobster and crab</p>
    <p class="item" style="font-weight:700">Large or Colossal</p>
  </div>

  <div class="section" style="top:445px;left:40px;width:262px">
    <h2 class="section-title">Special Rolls</h2>
    <p class="item"><span class="item-name">The Harbor</span> : tuna, salmon, yellowtail, avocado, spicy mayo, soy bean paper</p>
    <p class="item"><span class="item-name">King Crab Rainbow</span> : king crab, avocado, assorted fish on top</p>
    <p class="item"><span class="item-name">Empress</span> : shrimp tempura, spicy tuna on top, eel sauce</p>
    <p class="item"><span class="item-name">Spicy Girl</span> : spicy crunchy crab meat, cucumber, shrimp on top</p>
    <p class="item"><span class="item-name">Dragon</span> : eel, cucumber, avocado, tobiko on top, eel sauce</p>
    <p class="item"><span class="item-name">Yummy</span> : spicy crunchy salmon, avocado, mango, salmon on top</p>
    <p class="item"><span class="item-name">No. 9</span> : shrimp tempura, avocado, aioli, spicy mayo, tobiko</p>
    <p class="item"><span class="item-name">Sunrise Roll</span> : spicy crunchy tuna and avocado, salmon on top</p>
  </div>

  <div class="photo photo--platter" role="img" aria-label="Black and white photo of a seafood platter on ice"></div>

  <div class="section" style="top:620px;left:40px;width:300px">
    <h2 class="section-title">Apps</h2>
    <p class="item"><span class="item-name">BAO Bun</span> ; hoisin bbq pancetta cut pork loin, crispy onions, micro mint</p>
    <p class="item"><span class="item-name">Five Spice Crispy Popcorn Crusted Prawns (2)</span> ; classic burre blanc</p>
    <p class="item"><span class="item-name">Jumbo Lump Crab</span> ; citrus miso drizzle, spring pea puree, micro greens</p>
  </div>
</section>

<section class="menu-page menu-page--grill" aria-label="Steaks and entrees page">
  <div class="page-tab"></div>
  <div class="dotted-rule"></div>
  <span class="corner-mark corner-mark--tl"></span><span class="corner-mark corner-mark--tr"></span>
  <span class="corner-mark corner-mark--bl"></span><span class="corner-mark corner-mark--br"></span>

  <div class="photo photo--steak" role="img" aria-label="Black and white photo of a sliced grilled steak"></div>

  <div class="section plain-list" style="top:40px;left:44px;width:180px">
    <h2 class="section-title">USDA Prime Steaks</h2>
    <p class="item">10 Oz Filet</p>
    <p class="item">14 or 16 Oz New York Strip</p>
    <p class="item">24 Oz Boneless Ribeye</p>
    <p class="item">36 Oz Bone in Rib Eye</p>
    <p class="item">Berkshire Pork Chop</p>
  </div>
  <div class="section plain-list" style="top:140px;left:44px;width:180px">
    <h2 class="section-title">Sauces</h2>
    <p class="item">Cabernet Demi Glaz</p>
    <p class="item">Gorganzola Brulle Cream</p>
    <p class="item">Truffles Wild Mushroom Ragu</p>
    <p class="item">Horseradish Cream</p>
    <p class="item">House Steak Sauce</p>
  </div>
  <div class="section plain-list" style="top:40px;left:236px;width:300px">
    <h2 class="section-title">Sides</h2>
    <p class="item">Mashed Idaho Potatoes</p>
    <p class="item">Bacon, Sweet Corn, Caramelized Onion Fingerling Potatoes</p>
    <p class="item">Roasted Peanut Potatoes</p>
    <p class="item">Creamed Spinach</p>
    <p class="item">Sauteed Spinach</p>
    <p class="item">Grilled Asparagus</p>
    <p class="item">French Beans</p>
    <p class="item">Israeli Cous Cous</p>
    <p class="item">Sweet Potato Steak Fries</p>
    <p class="item">Corn Skillet</p>
  </div>

  <div class="section" style="top:320px;left:44px;width:490px">
    <p class="item"><span class="item-name">Classic Wedge</span> ; blue cheese, bacon lardons, heirloom tomatoes</p>
    <p class="item"><span class="item-name">Mixed Baby Greens</span> ; heirloom tomatoes, cucumber, red onion, dijon vinaigrette</p>
    <p class="item"><span class="item-name">Tabbouleh</span> ; buckwheat grain, fresh mint, tomato concasse, cucumber, parsley, lemon, EVOO</p>
    <p class="item"><span class="item-name">Tomato Mozzarella Salad / Burrata</span></p>
    <p class="item"><span class="item-name">Spinach Salad</span> ; green apple, feta, currants, with persimmons vinaigrette</p>
    <p class="item"><span class="item-name">Kale Caesar</span> ; homemade cacio e pepe dressing, pecorino and parmesan cheese, toasted croutons</p>
  </div>

  <div class="section" style="top:436px;left:44px;width:490px">
    <h2 class="section-title">Entrees</h2>
    <p class="item"><span class="item-name">Pan Roasted Miso Glazed Black Cod</span> ; green tea noodle stir fry, napa cabbage, carrot, japanese eggplant</p>
    <p class="item"><span class="item-name">Pan Seared Striped Bass</span> ; lobster succotash in a tomato saffron broth</p>
    <p class="item"><span class="item-name">EVOO Salted Grilled Swordfish</span> ; sun dried tomato, olive and caper tapenade, over basmati rice</p>
    <p class="item"><span class="item-name">Grilled Half Chicken</span> ; sundried tomato and basil israeli cous-cous, pan au jus</p>
    <p class="item"><span class="item-name">Roasted Fresh Cavatelle Ratatouille</span> ; vegetable broth</p>
    <p class="item"><span class="item-name">Lobster Cartoccio</span> ; shrimp, mussels, clams, fresh herb tomato broth, tossed with bucatini</p>
    <p class="item"><span class="item-name">Charred Artichoke Hearts</span> ; heirloom tomatoes, caper berries, spring onions, fresh basil, white wine reduction over forbidden rice (gf)</p>
    <p class="item"><span class="item-name">Mediterranean Grilled Veggie Plate</span> ; artichoke heart, japanese eggplant, green &amp; white asparagus, seared heirloom tomatoes, roasted baby carrots, cauliflower rice, evoo &amp; fig drizzle (gf)</p>
  </div>

  <div class="brand-name brand-name--foot">HARBOR<br><span style="font-size:11px;letter-spacing:4px">SUSHI &amp; STEAK</span></div>
</section>

</body>
</html>
```